Web Design Project

My website was fine - years ago. But it's way, way overdue for an overhaul. When I started my business almost 20 years ago, I wanted to be edgy. And my website was just that. Color, style, voice. Edgy. Today, my clients are corporations. I'm older, more experienced - but still a little edgy. It's controlled edge. What I want now is sophisticated. Savvy. Corporate but cool. Grown up.

My clients are primarily - but not exclusively - in healthcare. But I don't want a healthcare site. I provide the following services:
1. Writing - white papers, brochures, web pages, speechwriting, etc.
2. Marketing strategy
3. Public relations services
4. Thought leader development
5. Training
I couldn't upload all the icons but I can send them. They correspond with the pages as follows and should be used in the design:

1. Writing- nib.png
2. Marketing strategy-compass.png
3. Public relations services-microphone.png
4. Thought leader development-lightbulb.png
5. Training: cogs-training.png or key.png

I will have a blog, and a portfolio of some kind.

I don't want something that looks like a template.
Updates

Project Deadline Extended
Reason: Just made this a committed payment. I apologize for not doing so from the start. Nobody should work for free.

Project Deadline Extended
Reason: Several folks have asked to resubmit, and it has taken me a while to provide feedback.

Dear Designers,

I am so sorry to have been so slow to select. I've had professional and personal issues to deal with. I am actively trying to select a design, however, and will do so in the next two days. Thanks so much for your patience and hard work.

Marla

Thanks so much to everyone who has submitted a design. I had great luck crowdsourcing my logo, but I'm starting to realize that website design is a totally different animal. All of your designs are great, but they all look exactly like templates. And maybe that's the way it's supposed to be, the way it should be. I don't want to use stock photography. It needs to be more personalized than that. I'm open to illustration or even using my own photo on the site, but stock photography won't work for me. If anyone wants to submit something else - and I understand if you don't - please feel free. 

Target Market(s)

C-suite executives; corporations, larger businesses who need marketing writing

Industry/Entity Type

Healthcare

Requirements
Must have
• Logo (somewhere)
Icons
Nice to have
• Level-specific page design (e.g, Home = Level 1, Tabs = Level 2, etc). I'd like it to have a certain order.

```html
<!DOCTYPE html>
<html lang="en">
<head>
<meta charset="utf-8">
<title>Services</title>
<link rel="stylesheet" href="https://fonts.googleapis.com/css2?family=Poppins:wght@600&display=swap">
<style>
  :root {
    --band-plum: #7e4170;
    --band-sand: #d8cbae;
    --rule-amber: #f0a300;
    --disc-violet: #8b2487;
    --disc-violet-deep: #5e1660;
    --disc-violet-light: #b04aae;
    --ink-light: #ffffff;
    --ink-dark: #231f20;
  }
  html, body {
    margin: 0;
    padding: 0;
    overflow: hidden;
    background: var(--band-sand);
  }
  .services {
    display: block;
    width: 1200px;
    height: 637px;
  }
  .band--plum { fill: var(--band-plum); }
  .band--sand { fill: var(--band-sand); }
  .rule { fill: var(--rule-amber); }
  .badge__ring { fill: var(--rule-amber); }
  .badge__rim { fill: var(--disc-violet); }
  .badge__edge { fill: none; stroke: var(--rule-amber); stroke-width: 3; }
  .service-title {
    font-family: "Poppins", "Century Gothic", sans-serif;
    font-weight: 600;
    font-size: 52px;
  }
  .service-title--light { fill: var(--ink-light); }
  .service-title--dark { fill: var(--ink-dark); }
</style>
</head>
<body>
<svg class="services" viewBox="0 0 1200 637" width="1200" height="637" xmlns="http://www.w3.org/2000/svg">
  <defs>
    <radialGradient id="icon-field" cx="40%" cy="35%" r="70%">
      <stop offset="0" stop-color="var(--disc-violet-light)"/>
      <stop offset="0.6" stop-color="var(--disc-violet)"/>
      <stop offset="1" stop-color="var(--disc-violet-deep)"/>
    </radialGradient>
  </defs>

  <!-- service bands -->
  <rect class="band--plum" x="0" y="0" width="1200" height="109"/>
  <rect class="rule" x="0" y="109" width="1200" height="9"/>
  <rect class="band--sand" x="0" y="118" width="1200" height="167"/>
  <rect class="rule" x="0" y="285" width="1200" height="9"/>
  <rect class="band--plum" x="0" y="294" width="1200" height="163"/>
  <rect class="rule" x="0" y="457" width="1200" height="9"/>
  <rect class="band--sand" x="0" y="466" width="1200" height="163"/>
  <rect class="rule" x="0" y="629" width="1200" height="8"/>

  <!-- marketing strategy -->
  <g class="badge">
    <circle class="badge__ring" cx="158" cy="27" r="115"/>
    <circle class="badge__rim" cx="158" cy="27" r="100"/>
    <circle class="badge__edge" cx="158" cy="27" r="92"/>
    <circle cx="158" cy="27" r="88" fill="url(#icon-field)" role="img" aria-label="Compass icon for marketing strategy"/>
  </g>
  <text class="service-title service-title--light" x="321" y="49">Marketing strategy</text>

  <!-- thought leader development -->
  <g class="badge">
    <circle class="badge__ring" cx="1040" cy="201" r="115"/>
    <circle class="badge__rim" cx="1040" cy="201" r="100"/>
    <circle class="badge__edge" cx="1040" cy="201" r="92"/>
    <circle cx="1040" cy="201" r="88" fill="url(#icon-field)" role="img" aria-label="Lightbulb icon for thought leader development"/>
  </g>
  <text class="service-title service-title--dark" x="904" y="223" text-anchor="end">Thought leader development</text>

  <!-- training -->
  <g class="badge">
    <circle class="badge__ring" cx="142" cy="376" r="115"/>
    <circle class="badge__rim" cx="142" cy="376" r="100"/>
    <circle class="badge__edge" cx="142" cy="376" r="92"/>
    <circle cx="142" cy="376" r="88" fill="url(#icon-field)" role="img" aria-label="Key icon for training"/>
  </g>
  <text class="service-title service-title--light" x="287" y="398">Training</text>

  <!-- public relations services -->
  <g class="badge">
    <circle class="badge__ring" cx="1040" cy="545" r="115"/>
    <circle class="badge__rim" cx="1040" cy="545" r="100"/>
    <circle class="badge__edge" cx="1040" cy="545" r="92"/>
    <circle cx="1040" cy="545" r="88" fill="url(#icon-field)" role="img" aria-label="Cogs icon for public relations services"/>
  </g>
  <text class="service-title service-title--dark" x="902" y="568" text-anchor="end">Public relations services</text>
</svg>
</body>
</html>
```